Graphic Design for a block-note A4 size

We need a graphic design for a simple block-note A4 size. The product consists of 50 sheets in VERTICAL A4 (21x29,7cm) size, simply glued on top, without cover. We would like to have proposals with double application: one for home users without a logo and one for professionals with an area "put your logo here".
The graphics should be simple and attractive, elegant and pleasant to keep on your desk.
The block-notes may have standard squares (5 or 10 mm) or stripes (10 mm spaced) on the background to make the writing easy.
Feel free to use your creativity, the only limit is the CMYK color space.

We will upload some block-note simple templates and 3D sample images to help you.

Reason: We want to give you more few days to work on your graphic designs.

Industry/Entity Type

Graphic Design

Requirements
Must have
• The graphics should be simple and attractive, elegant and pleasant to keep on your desk.

Nice to have
• The block-notes may have standard squares (5 or 10 mm) or stripes (10 mm spaced) on the background to make the writing easy.

```html
<!DOCTYPE html>
<html lang="en">
<head>
<meta charset="utf-8">
<title>Block-note A4 – Home and Professional Editions</title>
<link rel="stylesheet" href="https://fonts.googleapis.com/css2?family=Tenor+Sans&display=swap">
<style>
  :root {
    --backdrop-light: #0a6cc4;
    --backdrop-dark: #063a73;
    --sheet: #ffffff;
    --grid-line: #dedede;
    --tri-pale: #cfe9f2;
    --tri-mid: #7fcdec;
    --tri-deep: #2e9fe0;
    --logo-text: #6b6b6b;
  }
  * { margin: 0; padding: 0; box-sizing: border-box; }
  html, body { width: 1200px; height: 848px; overflow: hidden; }
  body {
    position: relative;
    background: radial-gradient(ellipse at 20% 10%, var(--backdrop-light) 0%, #0857a6 45%, var(--backdrop-dark) 100%);
    font-family: "Tenor Sans", sans-serif;
  }
  .sheet {
    position: absolute;
    top: 67px;
    width: 492px;
    height: 697px;
    background: var(--sheet);
    box-shadow: 6px 8px 14px rgba(0, 20, 60, 0.35);
    overflow: hidden;
  }
  .sheet--home { left: 78px; }
  .sheet--pro { left: 621px; }
  .sheet__grid {
    position: absolute;
    left: 22px;
    top: 23px;
    width: 448px;
    height: 674px;
    border-top: 1px solid var(--grid-line);
    border-left: 1px solid var(--grid-line);
    background-image:
      linear-gradient(to right, var(--grid-line) 1px, transparent 1px),
      linear-gradient(to bottom, var(--grid-line) 1px, transparent 1px);
    background-size: 23.5px 23.5px;
    background-position: -1px -1px;
    border-right: 1px solid var(--grid-line);
  }
  .sheet__pattern {
    position: absolute;
    left: 0;
    top: 0;
    width: 492px;
    height: 697px;
  }
  .logo-area {
    position: absolute;
    left: 294px;
    top: 508px;
    color: var(--logo-text);
    line-height: 1;
  }
  .logo-area__small {
    display: block;
    font-size: 28px;
    letter-spacing: 0.5px;
  }
  .logo-area__large {
    display: block;
    font-size: 44px;
    letter-spacing: 1px;
    margin-top: 4px;
  }
</style>
</head>
<body>
  <svg width="0" height="0" style="position:absolute">
    <defs>
      <linearGradient id="tri-fade" x1="0" y1="0" x2="0.6" y2="1">
        <stop offset="0" stop-color="var(--tri-pale)"/>
        <stop offset="0.55" stop-color="var(--tri-mid)"/>
        <stop offset="1" stop-color="var(--tri-deep)"/>
      </linearGradient>
    </defs>
  </svg>

  <section class="sheet sheet--home" aria-label="Home edition sheet">
    <div class="sheet__grid"></div>
    <svg class="sheet__pattern" viewBox="0 0 492 697" role="img" aria-label="Scattered blue triangle mosaic rising from the lower left corner">
      <polygon points="0,378 40,382 70,470 90,540 150,555 200,553 260,600 330,595 400,625 492,640 492,697 0,697" fill="url(#tri-fade)" opacity="0.75"/>
    </svg>
  </section>

  <section class="sheet sheet--pro" aria-label="Professional edition sheet">
    <div class="sheet__grid"></div>
    <svg class="sheet__pattern" viewBox="0 0 492 697" role="img" aria-label="Scattered blue triangle mosaic rising from the lower left corner">
      <polygon points="0,378 40,382 70,470 90,540 150,555 200,553 260,600 330,595 400,625 492,640 492,697 0,697" fill="url(#tri-fade)" opacity="0.75"/>
    </svg>
    <div class="logo-area">
      <span class="logo-area__small">your logo</span>
      <span class="logo-area__large">HERE</span>
    </div>
  </section>
</body>
</html>
```